Recently launched Investment banking and Corporate Advisory firm focused and experienced on Selling

We are looking for a dynamic Brochure that can highlight our areas of focus, experience and expertise.
We have a small but seasoned team of professionals in the organisation and want to showcase our ability to provide Growth and / or exit solutions for our clients.
We are a boutique firm and want to focus on showcasing the fact that we strive for excellence and quality and not quantity.

Our core business avtivity at this time is Sell Side M&A services (this means that we sell private businesses). We are unique in our approach to "partnering businesses" with other companies...not just selling them. We focus more on the "strategic fit" of the potential partner rather than the simple valuation that a potential partner (buyer) would place on the company.

We have really been focusing on "GROWTH and EXIT" strategies for private business owners. Customers usually talk to us for 1 of two main reasons. Their businesses are usually very stable or rapidly growing , often to a point where the owners are no longer comfortable running them on their own. They often need capital for expansion or a team to help them expand their business into other countries and markets. for this we look for a solution for them and often it is finding them a strategic partner who will want to buy the majority of the business. There are also the clients that are looking for an exit strategy (typically they are older and getting ready to retire) they are typically seeking for a way to exit the business (sell the business).

A tagline I often use is "Customer Vision" - We see our customers business and needs through their eyes.

Our company website is www.keldmoorpartners.com and is a work in progress

Target Market(s)

Business Owners (CEO / Presidents)
Mostly Male
Late 40's to late 60's
Very often they will be Engineers
Very Successful and hard working
Many of them looking for GROWTH solutions
Many of them looking for Retirement
We heavily focus on Oil and Gas Service companies, Oil and Gas manufacturing / oilfield services / Technology Companies and Industrial Companies

Industry/Entity Type

Boutique

Font styles to use
Sans Serif

Colors
f37022
33a6d7

Requirements
Must have
• This must be extremely high quality. The people that will receive these brochures are Presidents and CEO's of companies. Every document we give the customer directly reflects the quality of service we will provide for them.
Nice to have
• Pictures tell a great story and can also tell about the areas of experience and expertise that we have

Ideally we'd be interested in a square shaped marketing document (signifies strength and solidness in the business/opportunity) - either 5x5 or 7x7 size in a 4-6 page (double-sided) saddle-stitched booklet.
We'd like to relay an emotion while also describing our business.

```html
<!DOCTYPE html>
<html lang="en">
<head>
<meta charset="utf-8">
<title>Merger &amp; Acquisition Advisory Service</title>
<link rel="stylesheet" href="https://fonts.googleapis.com/css2?family=Inter:wght@300;400;600&display=swap">
<style>
  :root {
    --page-bg: #ffffff;
    --frame-line: #3a3a3a;
    --heading-blue: #1b78c8;
    --body-text: #2b2b2b;
    --title-white: #ffffff;
    --photo-dark: #3c4452;
    --photo-mid: #8a8e98;
    --photo-skin: #e8b9a4;
    --photo-light: #efe7e2;
  }
  html, body {
    margin: 0;
    padding: 0;
    width: 1200px;
    height: 600px;
    overflow: hidden;
    background: var(--page-bg);
  }
  .spread {
    position: relative;
    width: 1200px;
    height: 600px;
    font-family: "Inter", Arial, sans-serif;
    color: var(--body-text);
  }
  .cover-panel {
    position: absolute;
    left: 0;
    top: 0;
    width: 598px;
    height: 598px;
    border: 1px solid var(--frame-line);
    box-sizing: border-box;
  }
  .cover-photo {
    position: absolute;
    left: 15px;
    top: 15px;
    width: 570px;
    height: 570px;
    background:
      radial-gradient(ellipse 40% 45% at 55% 50%, var(--photo-skin) 0%, rgba(232,185,164,0.6) 55%, rgba(232,185,164,0) 100%),
      radial-gradient(ellipse 30% 40% at 90% 20%, var(--photo-light) 0%, rgba(239,231,226,0) 100%),
      linear-gradient(160deg, var(--photo-dark) 0%, var(--photo-mid) 45%, var(--photo-dark) 75%, #c9a98d 100%);
  }
  .cover-title {
    position: absolute;
    left: 44px;
    top: 38px;
    margin: 0;
    font-weight: 300;
    font-size: 52px;
    line-height: 52px;
    letter-spacing: -0.5px;
    color: var(--title-white);
    text-transform: uppercase;
  }
  .service-copy {
    position: absolute;
    left: 643px;
    top: 40px;
    width: 360px;
    font-size: 12px;
    line-height: 17px;
  }
  .service-heading {
    margin: 0;
    font-weight: 600;
    font-size: 12px;
    line-height: 16px;
    color: var(--heading-blue);
    text-transform: uppercase;
  }
  .service-intro {
    margin: 0 0 17px;
  }
  .services-lead {
    margin: 0 0 4px;
  }
  .services-list {
    list-style: none;
    margin: 0;
    padding: 0;
  }
  .services-list li {
    position: relative;
    padding-left: 14px;
    line-height: 18.8px;
  }
  .services-list li::before {
    content: "";
    position: absolute;
    left: 2px;
    top: 7px;
    width: 5px;
    height: 5px;
    border-radius: 50%;
    background: var(--body-text);
  }
</style>
</head>
<body>
  <main class="spread">
    <section class="cover-panel">
      <div class="cover-photo" role="img" aria-label="Close-up of two businesspeople in suits shaking hands"></div>
      <h1 class="cover-title">Merger &amp;<br>Acquisition</h1>
    </section>

    <section class="service-copy">
      <h2 class="service-heading">Merger and Acquisition Advisory Service</h2>
      <p class="service-intro">Patilin sessa qua mus ari publiuritam, num hostri peris erae, eribunu me re, nosu ius, tum serios, crionve rviverterra, cre cae apecto ium publis me accidem nonsus nihicae erestiam factas. Catuam nontis culego ubli, uscitam moritat quondum estam huctudet gra vissilic fuiu mei con ta pra senirmius a nossi sentilicis.</p>
      <p class="services-lead">Our services include:</p>
      <ul class="services-list">
        <li>Synergy business plans</li>
        <li>Recast financial</li>
        <li>Brief writing and generation</li>
        <li>Extensive research</li>
        <li>Business intelligence reports</li>
        <li>Market studies/reports</li>
        <li>Feasibility studies</li>
        <li>Coaching and mentoring</li>
        <li>Contract negotiations</li>
        <li>Due diligence facilitation</li>
        <li>Project management</li>
        <li>Financial business plans</li>
        <li>Prospectus/Information memorandum</li>
        <li>writing and generation</li>
        <li>Detailed research lists</li>
        <li>Outbound prospect generation</li>
      </ul>
    </section>
  </main>
</body>
</html>
```